New corporate e-mail signature

We need a new e-mail signature for our company that is clean and professional. The requests are attached in a document.

Target Market(s)

CFO, CTO, Controllers, leaders, decision-makers.

Industry/Entity Type

Information Technology

Colors

Designer to choose colors to be used in the design.

Requirements
Must have
• See the PowerPoint document.
• - keep it as simple as possible.
• - same style as our new website design
• - It has to look good in all e-mail readers, and on all surfaces.
Nice to have
• - Please also attach 'best practise' for how to use the signature.
Should not have
• See the PowerPoint document. Use our color palette.
• - Do not include photo!

```html
<!DOCTYPE html>
<html lang="en">
<head>
<meta charset="utf-8">
<title>Email Signature – Brightledger</title>
<link href="https://fonts.googleapis.com/css2?family=Montserrat:wght@500;600;700&display=swap" rel="stylesheet">
<style>
  :root {
    --brand-teal: #1a7898;
    --text-grey: #4a4a4a;
    --card-border: #cfe0e6;
    --page-bg: #ffffff;
    --on-brand: #ffffff;
  }
  * { box-sizing: border-box; margin: 0; padding: 0; }
  html, body {
    width: 1200px; height: 1038px; overflow: hidden;
    background: var(--page-bg);
    font-family: "Montserrat", Arial, sans-serif;
  }
  .canvas { position: relative; width: 1200px; height: 1038px; }
  .signature {
    position: absolute; left: 77px; top: 377px;
    width: 1057px; height: 320px;
    border: 1px solid var(--card-border);
    background: var(--page-bg);
  }
  .identity { position: absolute; left: 84px; top: 80px; }
  .identity__name {
    font-size: 35px; font-weight: 700; color: var(--brand-teal);
    letter-spacing: 0.2px; line-height: 1.2;
  }
  .identity__role {
    margin-top: 4px; font-size: 25px; font-weight: 500; color: var(--text-grey);
  }
  .divider {
    position: absolute; left: 497px; top: 33px;
    width: 3px; height: 172px;
    background: linear-gradient(to bottom, transparent, var(--brand-teal) 12%, var(--brand-teal) 88%, transparent);
    border-radius: 2px;
  }
  .contact { position: absolute; left: 623px; top: 78px; list-style: none; }
  .contact__item {
    display: flex; align-items: center; gap: 14px;
    font-size: 24px; font-weight: 500; color: var(--brand-teal);
    height: 32px;
  }
  .contact__item + .contact__item { margin-top: 25px; }
  .contact__icon { width: 24px; height: 24px; fill: var(--brand-teal); flex: none; }
  .footer-band {
    position: absolute; left: 0; bottom: 0; width: 100%; height: 81px;
    background: var(--brand-teal); color: var(--on-brand);
  }
  .footer-band__brand {
    position: absolute; left: 108px; top: 22px;
    font-size: 30px; font-weight: 700; color: var(--on-brand); letter-spacing: -0.3px;
  }
  .footer-band__web {
    position: absolute; left: 416px; top: 30px;
    font-size: 17px; font-weight: 500; letter-spacing: 0.2px;
  }
  .social { position: absolute; left: 781px; top: 24px; display: flex; gap: 48px; list-style: none; }
  .social__link {
    display: block; width: 34px; height: 34px; border-radius: 50%;
    background: var(--on-brand);
  }
</style>
</head>
<body>
<main class="canvas">
  <section class="signature">
    <div class="identity">
      <p class="identity__name">Daniel Hartwell</p>
      <p class="identity__role">Business Analyst</p>
    </div>
    <div class="divider"></div>
    <ul class="contact">
      <li class="contact__item">
        <svg class="contact__icon" viewBox="0 0 24 24" aria-hidden="true">
          <path d="M1 5h22v14H1z M2.5 6.2 12 13l9.5-6.8v1.6L12 14.6 2.5 7.8z" fill-rule="evenodd"/>
        </svg>
        hello@brightledger.com
      </li>
      <li class="contact__item">
        <svg class="contact__icon" viewBox="0 0 24 24" aria-hidden="true">
          <path d="M6.6 10.8a15.1 15.1 0 0 0 6.6 6.6l2.2-2.2c.3-.3.7-.4 1-.2 1.1.4 2.3.6 3.6.6.6 0 1 .4 1 1V20c0 .6-.4 1-1 1A17 17 0 0 1 3 4c0-.6.4-1 1-1h3.5c.6 0 1 .4 1 1 0 1.3.2 2.5.6 3.6.1.3 0 .7-.2 1z"/>
        </svg>
        001 555 014 273
      </li>
    </ul>
    <footer class="footer-band">
      <span class="footer-band__brand">brightledger</span>
      <span class="footer-band__web">www.brightledger.com</span>
      <ul class="social">
        <li><span class="social__link" role="img" aria-label="Professional network profile link"></span></li>
        <li><span class="social__link" role="img" aria-label="Microblog profile link"></span></li>
        <li><span class="social__link" role="img" aria-label="Video channel link"></span></li>
      </ul>
    </footer>
  </section>
</main>
</body>
</html>
```